Improvement of design for elearning template

Our company provides web based elearning courses for employees. We have a design layout for the different slides which can be found here: https://www.filecrate-share.com/sh/qemvirt7xnoa2lup/KLpQzRtYwMbDfHsnVcEkGaUoPi?dl=0. The content will be added later. At this point we are just looking for a design layout that works with different content types like images, text, quiz & videos. What we would ask you, is to pick randomly 1 or 2 of the elearning slides from the existing designs and suggest improvements or come up with an alternative design. The winner of the design project can work on all slides and this will be a project with a much larger budget.
Target Market(s)
Employees in large enterprises
Look and feel
Each slider illustrates characteristics of the customer's brand and the style your logo design should communicate.

```html
<!DOCTYPE html>
<html lang="en">
<head>
<meta charset="utf-8">
<title>eLearning Slide Layout – Board 2 of 2</title>
<link href="https://fonts.googleapis.com/css2?family=Montserrat:ital,wght@0,400;0,500;0,600;0,700;1,600&display=swap" rel="stylesheet">
<style>
  :root{
    --green:#3ab54a;
    --navy:#23278a;
    --text:#4a4a4a;
    --muted:#7a7a7a;
    --line:#dcdcdc;
    --sky:#e8f4fb;
    --sky-line:#b5dff2;
    --overlay:#dddddd;
    --overlay-edge:#b9b9b9;
    --brand-blue:#2aa6e0;
    --brand-grey:#b8b8b8;
    --bar-green:#4fb07a;
  }
  *{margin:0;padding:0;box-sizing:border-box}
  html,body{width:1200px;height:1200px;overflow:hidden;background:#fff}
  body{font-family:"Montserrat",sans-serif;color:var(--text);position:relative}

  .board-label{position:absolute;left:80px;top:52px;font-size:16px;font-weight:500;color:var(--green)}
  .note{position:absolute;font-size:12.2px;line-height:14px;color:var(--green)}
  .note--overlay{left:914px;top:192px}
  .note--nav{left:68px;top:574px}

  .flows{position:absolute;left:0;top:0;width:1200px;height:1200px;pointer-events:none}

  .frame{position:absolute;background:#fff;border:1px solid var(--line);overflow:hidden}
  .wave{position:absolute;left:0;top:0;width:100%;height:100%}
  .menu-icon{position:absolute;display:flex;flex-direction:column;justify-content:space-between}
  .menu-icon span{display:block;height:1.3px;background:#7d7d7d}
  .chevron{position:absolute}
  .brand-square{position:absolute;background:var(--brand-blue)}
  .illustration{position:absolute;border-radius:6px;background:linear-gradient(135deg,#dbe8fb 0%,#7aa4ea 55%,#2c4fb8 100%)}

  /* mobile slide */
  .mobile{left:347px;top:132px;width:223px;height:483px}
  .mobile .brand-square{left:10px;top:13px;width:9px;height:9px}
  .mobile .slide-title{position:absolute;left:0;width:223px;top:15px;text-align:center;font-size:7px;font-weight:700;color:var(--navy)}
  .mobile .menu-icon{left:196px;top:13px;width:15px;height:10px}
  .mobile .lesson{position:absolute;left:9px;top:41px;font-size:11.3px;color:var(--navy)}
  .mobile .heading{position:absolute;left:10px;top:65px;width:200px;font-size:11.8px;line-height:13.5px;font-weight:700;color:var(--navy)}
  .mobile .body{position:absolute;left:10px;top:104px;width:205px;font-size:9.9px;line-height:14.3px}
  .mobile .bullets{position:absolute;left:22px;top:239px;width:180px;list-style:none;font-size:9.9px;line-height:14.3px;color:#333;font-weight:500}
  .mobile .bullets li{margin-bottom:1px}
  .mobile .closing{position:absolute;left:12px;top:344px;width:205px;font-size:9.9px;line-height:14.3px}
  .mobile .divider{position:absolute;left:12px;top:382px;width:195px;height:1px;background:var(--line)}
  .mobile .scroll-cue{position:absolute;left:18px;top:392px}
  .mobile .illustration{left:72px;top:395px;width:145px;height:88px}

  /* navigation overlay */
  .overlay{position:absolute;left:667px;top:112px;width:221px;height:481px;border:1px solid var(--line);background:#fff}
  .overlay .sheet{position:absolute;left:2px;top:2px;width:215px;height:475px;background:var(--overlay);border:2px solid var(--overlay-edge);border-radius:5px}
  .overlay .slide-title{position:absolute;left:0;width:215px;top:10px;text-align:center;font-size:7px;font-weight:700;color:var(--navy)}
  .overlay .close{position:absolute;left:193px;top:11px}
  .overlay .stat{position:absolute;left:16px;font-size:9.3px;color:#555}
  .overlay .stat b{color:var(--navy);font-weight:600}
  .progress-bar{position:absolute;left:16px;top:66px;width:145px;height:14px}
  .progress-bar .track{position:absolute;left:0;top:7px;width:145px;height:2px;background:#8a8a8a}
  .progress-bar .fill{position:absolute;left:0;top:2px;width:42px;height:12px;background:var(--bar-green)}
  .progress-bar .tick{position:absolute;top:0;width:1px;height:14px;background:#8a8a8a}
  .lessons{position:absolute;left:17px;top:155px;width:190px;list-style:none;font-size:8.6px;line-height:10px;color:#555}
  .lessons li{position:absolute;left:0;width:190px}
  .lessons .done{color:var(--green)}
  .lessons .current{color:var(--navy);font-weight:600}
  .lessons .current em{font-size:7.4px;font-weight:600;margin-left:3px}
  .overlay .illustration{left:70px;top:395px;width:140px;height:80px;opacity:.18}

  /* desktop slide */
  .desktop{left:212px;top:667px;width:787px;height:443px}
  .desktop .brand-square{left:52px;top:28px;width:10px;height:10px}
  .desktop .company{position:absolute;left:72px;top:24px;font-size:9.5px;font-weight:500;color:#8a8a8a}
  .desktop .slide-title{position:absolute;left:230px;width:324px;top:24px;text-align:center;font-size:12.4px;font-weight:700;color:var(--navy)}
  .desktop .menu-icon{left:743px;top:19px;width:21px;height:15px}
  .desktop .lesson{position:absolute;left:57px;top:72px;font-size:18.6px;color:var(--navy)}
  .desktop .heading{position:absolute;left:57px;top:117px;font-size:18.6px;font-weight:700;color:var(--navy)}
  .desktop .body{position:absolute;left:57px;top:152px;width:400px;font-size:10.3px;line-height:14.5px}
  .desktop .bullets{position:absolute;left:57px;top:231px;width:380px;list-style:none;font-size:10.3px;line-height:14.5px;font-weight:500;color:#333}
  .desktop .bullets li{margin-bottom:1.3px}
  .desktop .closing{position:absolute;left:57px;top:309px;font-size:10.3px}
  .desktop .illustration{left:481px;top:264px;width:305px;height:179px}
</style>
</head>
<body>

<p class="board-label">Board 2 of 2</p>

<p class="note note--overlay">In course navigation<br>and progress indicators<br>combined in one overlay.<br>Quick access to all data<br>without cluttering screen</p>
<p class="note note--nav">Next/back<br>navigation through<br>swipe gesture, or buttons</p>

<!-- mobile slide -->
<section class="frame mobile">
  <svg class="wave" viewBox="0 0 223 483" aria-hidden="true">
    <path d="M145 0 C175 40 170 120 150 180 C130 240 100 330 150 483 L223 483 L223 0 Z" fill="var(--sky)"/>
    <path d="M222 50 C220 140 150 180 130 260 C110 340 120 420 175 483" fill="none" stroke="var(--sky-line)" stroke-width="1"/>
  </svg>
  <div class="brand-square"></div>
  <h2 class="slide-title">Handling sensitive information</h2>
  <div class="menu-icon"><span></span><span></span><span></span></div>
  <h3 class="lesson">Lesson 2: Phishing awareness</h3>
  <h1 class="heading">Ad minim veniam, quis nostrud exerci tation</h1>
  <p class="body">Lorem ipsum dolor sit amet, consectetuer adipiscing elit, sed diam nonummy nibh euismod tincidunt ut laoreet dolore magna aliquam erat volutpat. Ut wisi enim ad minim veniam, quis nostrud exerci tation ullamcorper suscipit lobortis nisl ut aliquip ex ea commodo consequat. Duis autem vel eum</p>
  <ul class="bullets">
    <li>• Lorem ipsum dolor sit amet, consectetuer adipiscing elit,</li>
    <li>• Sed diam nonummy nibh eui smod tincidunt ut laoreet dolore magna aliquam erat volutpat.</li>
    <li>• Ut wisi enim ad minim veniam, quis nostrud.</li>
  </ul>
  <p class="closing">Lorem ipsum dolor sit amet, consectetuer adipiscing elit, sed diam</p>
  <div class="divider"></div>
  <svg class="scroll-cue" width="9" height="7" viewBox="0 0 9 7" aria-hidden="true"><path d="M0 0 H9 L4.5 7 Z" fill="#8a8a8a"/></svg>
  <svg class="chevron" style="left:7px;top:207px" width="8" height="28" viewBox="0 0 8 28" aria-hidden="true"><path d="M7 1 L1 14 L7 27" fill="none" stroke="#c8c8c8" stroke-width="1.2"/></svg>
  <svg class="chevron" style="left:207px;top:207px" width="8" height="28" viewBox="0 0 8 28" aria-hidden="true"><path d="M1 1 L7 14 L1 27" fill="none" stroke="#c8c8c8" stroke-width="1.2"/></svg>
  <div class="illustration" role="img" aria-label="Illustration: woman at a laptop with security shield, password field and email icons"></div>
</section>

<!-- navigation overlay -->
<section class="overlay">
  <div class="sheet">
    <h2 class="slide-title">Handling sensitive information</h2>
    <svg class="close" width="10" height="10" viewBox="0 0 10 10" aria-hidden="true"><path d="M1 1 L9 9 M9 1 L1 9" stroke="#555" stroke-width="1.3"/></svg>
    <p class="stat" style="top:48px">Progress <b>28%</b></p>
    <div class="progress-bar">
      <div class="track"></div>
      <div class="fill"></div>
      <div class="tick" style="left:0"></div>
      <div class="tick" style="left:23px"></div>
      <div class="tick" style="left:47px"></div>
      <div class="tick" style="left:70px"></div>
      <div class="tick" style="left:94px"></div>
      <div class="tick" style="left:118px"></div>
      <div class="tick" style="left:144px"></div>
    </div>
    <p class="stat" style="top:96px">Time <b>23 minutes | 0 hours | 0 days</b></p>
    <p class="stat" style="top:113px">Start date <b>07 July, 2021</b></p>
    <ul class="lessons">
      <li class="done" style="top:0">Lesson 1 : nonummy nibh
        <svg width="9" height="8" viewBox="0 0 9 8" aria-hidden="true" style="margin-left:5px"><path d="M1 4 L3.5 6.5 L8 1" fill="none" stroke="var(--green)" stroke-width="1.6"/></svg></li>
      <li class="current" style="top:15px">Lesson 2 : Phishing awareness <em>... ongoing</em></li>
      <li style="top:31px">Lesson 3 : Sed diam tincident utring<br>nisl ut consequat</li>
      <li style="top:60px">Test : Mid-course assessment</li>
      <li style="top:79px">Lesson 4 : Tincident utring nisl<br>ut consequat</li>
      <li style="top:107px">Lesson 5 : Erat ed diam tincident<br>utring nisl</li>
      <li style="top:133px">Lesson 6 : Utring nisl</li>
      <li style="top:151px">Test : Final assessment</li>
      <li style="top:170px">Glossary</li>
      <li style="top:201px">Exit course</li>
    </ul>
    <div class="illustration" role="img" aria-label="Faded slide illustration behind the overlay"></div>
  </div>
</section>

<!-- desktop slide -->
<section class="frame desktop">
  <svg class="wave" viewBox="0 0 787 443" aria-hidden="true">
    <path d="M580 0 C640 60 620 140 610 200 C595 300 610 380 600 443 L787 443 L787 0 Z" fill="var(--sky)"/>
    <path d="M702 0 C705 80 650 120 600 170 C540 230 520 300 560 380 C580 415 600 430 635 443" fill="none" stroke="var(--sky-line)" stroke-width="1.6"/>
  </svg>
  <div class="brand-square"></div>
  <span class="company">Company Name</span>
  <h2 class="slide-title">Handling sensitive information</h2>
  <div class="menu-icon"><span></span><span></span><span></span></div>
  <h3 class="lesson">Lesson 2: Phishing awareness</h3>
  <h1 class="heading">Ad minim veniam, quis nostrud exerci tation</h1>
  <p class="body">Lorem ipsum dolor sit amet, consectetuer adipiscing elit, sed diam nonummy nibh euismod tincidunt ut laoreet dolore magna aliquam erat volutpat. Ut wisi enim ad minim veniam, quis nostrud exerci tation ullamcorper suscipit lobortis nisl ut aliquip ex ea commodo consequat. Duis autem vel eum</p>
  <ul class="bullets">
    <li>● Lorem ipsum dolor sit amet, consectetuer adipiscing elit,</li>
    <li>● Sed diam nonummy nibh eui smod tincidunt ut laoreet dolore magna aliquam erat volutpat.</li>
    <li>● Ut wisi enim ad minim veniam, quis nostrud.</li>
  </ul>
  <p class="closing">Lorem ipsum dolor sit amet, consectetuer adipiscing elit, sed diam.</p>
  <svg class="chevron" style="left:16px;top:180px" width="16" height="56" viewBox="0 0 16 56" aria-hidden="true"><path d="M14 1 L2 28 L14 55" fill="none" stroke="#c8c8c8" stroke-width="1.8"/></svg>
  <svg class="chevron" style="left:745px;top:180px" width="16" height="56" viewBox="0 0 16 56" aria-hidden="true"><path d="M2 1 L14 28 L2 55" fill="none" stroke="#c8c8c8" stroke-width="1.8"/></svg>
  <div class="illustration" role="img" aria-label="Illustration: woman at a laptop with security shield, password field and email icons"></div>
</section>

<!-- flow arrows -->
<svg class="flows" viewBox="0 0 1200 1200" aria-hidden="true">
  <defs>
    <marker id="arrowhead" viewBox="0 0 10 10" refX="8" refY="5" markerWidth="6" markerHeight="6" orient="auto-start-reverse">
      <path d="M0 0 L10 5 L0 10 Z" fill="var(--green)"/>
    </marker>
  </defs>
  <path d="M551 140 C590 80 630 60 660 70 C680 75 693 84 700 94" fill="none" stroke="var(--green)" stroke-width="0.8" marker-end="url(#arrowhead)"/>
  <path d="M968 672 C975 560 990 330 900 306" fill="none" stroke="var(--green)" stroke-width="0.8" marker-end="url(#arrowhead)"/>
  <path d="M140 631 C140 740 160 810 223 860" fill="none" stroke="var(--green)" stroke-width="0.8" marker-end="url(#arrowhead)"/>
</svg>

</body>
</html>
```